New Business Cards for Organic Meat Farm

We need a business card designed for Thornbury Farm, a meat farm in western MA. Our logo uses a hand-drawn woodcut (attached). Our color palette has been simply black and white (shown in notepad and picture of our food truck). While we are based out of western MA, we have ambitions to grow nationally, so our hope is for a classy and memorable card which will be printed on a premium quality stock from a printer like printkestrel.com.
Target Market(s)
consumers of quality meats, restauranteurs, partnering farms
Industry/Entity Type
Farming and prepared meat products
Contact Information for Business Card
Wendell Pruitt, President/Owner, wendell@thornburyfarm.com, mobile: 413-555-0172, phone: 413-555-0148, thornburyfarm.com, facebook: @thornburyfarm, instagram: @thornburyfarmma
Colors
Designer to choose colors to be used in the design.
Look and feel

```html
<!DOCTYPE html>
<html lang="en">
<head>
<meta charset="utf-8">
<title>Thornbury Farm — Business Card</title>
<link rel="stylesheet" href="https://fonts.googleapis.com/css2?family=Montserrat:wght@600&family=Questrial&display=swap">
<style>
  :root {
    --backdrop: #a3a3a3;
    --paper: #ffffff;
    --ink: #141414;
    --ink-soft: #2a2a2a;
    --woodcut-dark: #2b2b2b;
    --woodcut-light: #8a8a8a;
  }
  * { box-sizing: border-box; margin: 0; padding: 0; }
  html, body {
    width: 1134px;
    height: 1200px;
    overflow: hidden;
    background: var(--backdrop);
  }
  .sheet {
    position: relative;
    width: 1134px;
    height: 1200px;
  }
  .card {
    position: absolute;
    left: 117px;
    width: 900px;
    height: 516px;
    background: var(--paper);
    color: var(--ink);
    font-family: "Questrial", sans-serif;
  }
  .card--front { top: 56px; }
  .card--back  { top: 628px; }

  /* Front */
  .front-illustration {
    position: absolute;
    left: 263px;
    top: 80px;
    width: 374px;
    height: 160px;
    border-radius: 190px 190px 8px 8px;
    background: radial-gradient(ellipse at 50% 40%, var(--woodcut-light) 0%, var(--woodcut-dark) 85%);
  }
  .wordmark {
    position: absolute;
    left: 0;
    right: 0;
    top: 268px;
    text-align: center;
    font-family: "Montserrat", sans-serif;
    font-weight: 600;
    font-size: 58px;
    letter-spacing: 0.5px;
    color: var(--ink);
  }

  /* Back */
  .back-frame {
    position: absolute;
    inset: 28px;
    border: 2px solid var(--ink);
  }
  .contact-name {
    position: absolute;
    left: 73px;
    top: 60px;
    font-family: "Montserrat", sans-serif;
    font-weight: 600;
    font-size: 36px;
    letter-spacing: 0.5px;
  }
  .contact-title {
    position: absolute;
    left: 73px;
    top: 108px;
    font-size: 22px;
    color: var(--ink-soft);
  }
  .back-illustration {
    position: absolute;
    right: 71px;
    top: 53px;
    width: 169px;
    height: 89px;
    border-radius: 90px 90px 4px 4px;
    background: radial-gradient(ellipse at 50% 40%, var(--woodcut-light) 0%, var(--woodcut-dark) 85%);
  }
  .contact-table {
    position: absolute;
    left: 73px;
    top: 248px;
    width: 756px;
    height: 86px;
    border-top: 3px solid var(--ink);
    border-bottom: 3px solid var(--ink);
    display: flex;
  }
  .contact-cell {
    display: flex;
    flex-direction: column;
    justify-content: center;
    align-items: center;
    font-size: 20px;
    line-height: 1.2;
  }
  .contact-cell--phones { width: 379px; border-right: 3px solid var(--ink); }
  .contact-cell--web { flex: 1; }
  .social {
    position: absolute;
    top: 405px;
    display: flex;
    align-items: center;
    gap: 8px;
    font-size: 20px;
    transform: translateX(-50%);
  }
  .social--facebook { left: 242px; }
  .social--instagram { left: 651px; }
  .social-dot {
    width: 12px;
    height: 12px;
    border-radius: 50%;
    background: var(--ink);
  }
</style>
</head>
<body>
<main class="sheet">
  <section class="card card--front">
    <div class="front-illustration" role="img" aria-label="Woodcut illustration of the farmhouse framed by trees"></div>
    <div class="wordmark">Thornbury Farm</div>
  </section>

  <section class="card card--back">
    <div class="back-frame"></div>
    <h1 class="contact-name">WENDELL PRUITT</h1>
    <p class="contact-title">President/Owner</p>
    <div class="back-illustration" role="img" aria-label="Small woodcut illustration of the farmhouse"></div>
    <div class="contact-table">
      <div class="contact-cell contact-cell--phones">
        <span>413-555-0172</span>
        <span>413-555-0148</span>
      </div>
      <div class="contact-cell contact-cell--web">
        <span>wendell@thornburyfarm.com</span>
        <span>thornburyfarm.com</span>
      </div>
    </div>
    <div class="social social--facebook"><span class="social-dot"></span><span>@thornburyfarm</span></div>
    <div class="social social--instagram"><span class="social-dot"></span><span>@thornburyfarmma</span></div>
  </section>
</main>
</body>
</html>
```